Professional Business Cards for Recruiting Company

We'd like professional 2-sided business cards that reflect a color scheme that matches our website, www.quillmerbay.com, and / or logo that is attached.

Slogan used is "We Know People", but needs to be editable because we change it up to "We Know Developers", "We Speak Geek", etc.

Must includes logo, slogan, first and last name, address, email, mobile number and website address.

Files attached for ideas.

Thanks!

Contact Information for Business Card

Logo, Company name, First name, Last name, addresss, email, phone, website address.

Font styles to use
Sans Serif

Colors
0054AA
0677BA
7BADD7
CADEEF
E8F1F8

Requirements
Nice to have
• I do like the following designs. 22962062 and 22962651. Couple ideas anyway.

```html
<!DOCTYPE html>
<html lang="en">
<head>
<meta charset="utf-8">
<title>Quillmerbay Business Cards</title>
<link href="https://fonts.googleapis.com/css2?family=Poppins:wght@300;400;500&display=swap" rel="stylesheet">
<style>
  :root {
    --canvas: #2a2a2a;
    --card: #232323;
    --card-edge: #1b1b1b;
    --pattern-light: #3a3a3a;
    --pattern-dark: #161616;
    --blue: #1f5fb8;
    --text-light: #d4d4d4;
    --text-mid: #a9a9a9;
    --rule: #8a8a8a;
  }
  * { box-sizing: border-box; margin: 0; padding: 0; }
  html, body { width: 1200px; height: 1015px; overflow: hidden; }
  body {
    background: var(--canvas);
    font-family: "Poppins", sans-serif;
    position: relative;
  }
  .card {
    position: absolute;
    left: 220px;
    width: 760px;
    height: 430px;
    background: var(--card);
    border: 1px solid var(--card-edge);
    box-shadow: 0 12px 30px rgba(0,0,0,.45);
    overflow: hidden;
  }
  .card--front { top: 60px; }
  .card--back { top: 525px; }

  /* Front */
  .front-texture {
    position: absolute; inset: 0;
    background: linear-gradient(135deg, var(--pattern-light) 0%, var(--card) 45%, var(--pattern-dark) 100%);
  }
  .front-brand {
    position: absolute; left: 50%; top: 50%;
    transform: translate(-50%, -50%);
    display: flex; flex-direction: column; align-items: center; gap: 18px;
    background: var(--card);
    padding: 26px 40px;
  }
  .brand-square {
    width: 46px; height: 46px;
    border: 2px solid var(--blue);
  }
  .brand-name {
    font-weight: 300;
    font-size: 38px;
    letter-spacing: 3px;
    color: var(--blue);
    text-transform: uppercase;
  }

  /* Back */
  .back-brand {
    position: absolute; left: 50px; top: 180px;
    display: flex; align-items: center; gap: 16px;
  }
  .back-brand .brand-square { width: 40px; height: 40px; }
  .back-brand .brand-name { font-size: 30px; letter-spacing: 2px; }
  .divider {
    position: absolute; left: 395px; top: 95px;
    width: 1px; height: 200px;
    background: var(--rule);
  }
  .divider::before {
    content: ""; position: absolute; left: 0; top: -50px;
    width: 2px; height: 42px; background: var(--blue);
  }
  .contact {
    position: absolute; left: 425px; top: 45px;
    color: var(--text-mid);
  }
  .contact-name {
    font-size: 22px; font-weight: 400; letter-spacing: 1px;
    text-transform: uppercase; color: var(--text-light);
  }
  .contact-name .first { color: var(--blue); }
  .contact-role {
    font-size: 13px; letter-spacing: 1px; text-transform: uppercase;
    margin-top: 2px;
  }
  .contact-list { list-style: none; margin-top: 22px; }
  .contact-list li {
    display: flex; align-items: center; gap: 10px;
    font-size: 15px; line-height: 26px;
  }
  .contact-list svg { width: 15px; height: 15px; flex: none; }
  .contact-address {
    font-size: 15px; line-height: 22px; margin-top: 18px; margin-left: 25px;
  }
  .slogan {
    position: absolute; left: 0; right: 0; bottom: 55px;
    text-align: center;
    font-size: 20px; letter-spacing: 1px;
    color: var(--blue); text-transform: uppercase;
    padding-left: 150px;
  }
</style>
</head>
<body>
  <section class="card card--front">
    <div class="front-texture" role="img" aria-label="Tonal repeating monogram pattern in dark grey gloss"></div>
    <div class="front-brand">
      <span class="brand-square"></span>
      <span class="brand-name">Quillmerbay</span>
    </div>
  </section>

  <section class="card card--back">
    <div class="back-brand">
      <span class="brand-square"></span>
      <span class="brand-name">Quillmerbay</span>
    </div>
    <span class="divider"></span>
    <div class="contact">
      <p class="contact-name"><span class="first">Dorian</span> Vasquell</p>
      <p class="contact-role">Managing Director</p>
      <ul class="contact-list">
        <li>
          <svg viewBox="0 0 16 16"><path d="M4 1.5l2.2 3-1.3 1.4c.8 1.9 2.3 3.4 4.2 4.2l1.4-1.3 3 2.2-1.2 2.5C7 13 3 9 2.5 2.7z" fill="var(--blue)"/></svg>
          044-555 010 275
        </li>
        <li>
          <svg viewBox="0 0 16 16"><rect x="1" y="3" width="14" height="10" fill="var(--blue)"/><path d="M1 3l7 6 7-6" stroke="var(--card)" stroke-width="1.3" fill="none"/></svg>
          info@quillmerbay.com
        </li>
        <li>
          <svg viewBox="0 0 16 16"><circle cx="8" cy="8" r="6.5" fill="none" stroke="var(--blue)" stroke-width="1.5"/><ellipse cx="8" cy="8" rx="2.8" ry="6.5" fill="none" stroke="var(--blue)" stroke-width="1.2"/><path d="M1.5 8h13" stroke="var(--blue)" stroke-width="1.2"/></svg>
          www.quillmerbay.com
        </li>
      </ul>
      <p class="contact-address">421, Address line goes here<br>45452, Country Name</p>
    </div>
    <p class="slogan">We Know People</p>
  </section>
</body>
</html>
```